Robotic Physical Therapy office needs a Grand Opening Flyer

We need a Grand Opening flyer design for a robotic physical therapy office named Stellar Motion Therapy. We would like it to have a clean, classy, upscale feeling that gives potential clients a V.I.P. feeling. We would like to use the colors black, gray, and yellow (logo will be uploaded).

Event: Thursday, June 1st, 2023 from 12pm-6pm
location: 58274 Harlow Ave, Bloomfield Hills, MI 48319

Industry/Entity Type

Physical therapy

Font styles to use
Script

Colors

Designer to choose colors to be used in the design.

Requirements
Nice to have
• More of a vip feel for the invite

```html
<!DOCTYPE html>
<html lang="en">
<head>
<meta charset="utf-8">
<title>Stellar Motion Therapy – Grand Opening</title>
<link rel="stylesheet" href="https://fonts.googleapis.com/css2?family=Great+Vibes&family=Open+Sans:wght@400;700&display=swap">
<style>
  :root {
    --bg: #3a3a44;
    --gold: #ffd814;
    --white: #ffffff;
    --red-light: #c41e45;
    --red-mid: #a01a2b;
    --red-dark: #741016;
  }
  * { margin: 0; padding: 0; box-sizing: border-box; }
  html, body { width: 927px; height: 1200px; overflow: hidden; background: var(--bg); }
  .flyer {
    position: relative;
    width: 927px;
    height: 1200px;
    background: var(--bg);
    color: var(--white);
    font-family: "Open Sans", sans-serif;
  }
  .brand {
    position: absolute;
    top: 106px;
    left: 0;
    width: 100%;
    display: flex;
    justify-content: center;
    align-items: center;
    gap: 10px;
  }
  .brand-dot {
    width: 30px;
    height: 30px;
    border-radius: 50%;
    background: var(--gold);
  }
  .brand-name {
    font-family: "Open Sans", sans-serif;
    font-weight: 700;
    font-size: 24px;
    letter-spacing: 0.5px;
    color: var(--white);
    text-transform: uppercase;
  }
  .banner {
    position: absolute;
    left: 187px;
    top: 281px;
    width: 554px;
    height: 323px;
    background:
      radial-gradient(ellipse at 55% 45%, var(--red-light) 0%, var(--red-mid) 45%, var(--red-dark) 100%);
    box-shadow: 0 10px 30px rgba(0,0,0,0.35);
  }
  .banner-title {
    position: absolute;
    left: 187px;
    top: 281px;
    width: 554px;
    height: 323px;
  }
  .title-grand {
    position: absolute;
    right: 40px;
    top: 93px;
    font-family: "Open Sans", sans-serif;
    font-weight: 700;
    font-size: 60px;
    line-height: 1;
    color: var(--gold);
    letter-spacing: -1px;
  }
  .title-opening {
    position: absolute;
    left: 40px;
    top: 110px;
    font-family: "Great Vibes", cursive;
    font-size: 128px;
    line-height: 1;
    color: var(--gold);
  }
  .invite-text {
    position: absolute;
    left: 127px;
    top: 684px;
    width: 673px;
    text-align: center;
    font-family: "Great Vibes", cursive;
    font-size: 33px;
    line-height: 46px;
    color: var(--white);
  }
  .detail {
    position: absolute;
    left: 0;
    width: 100%;
    text-align: center;
  }
  .detail-label {
    font-family: "Great Vibes", cursive;
    font-size: 54px;
    line-height: 1;
    color: var(--gold);
  }
  .detail-value {
    font-size: 16.5px;
    color: var(--white);
    margin-top: 2px;
  }
  .detail-event { top: 948px; }
  .detail-location { top: 1036px; }
</style>
</head>
<body>
  <main class="flyer">
    <header class="brand">
      <span class="brand-dot"></span>
      <span class="brand-name">Stellar Motion Therapy</span>
    </header>

    <div class="banner" role="img" aria-label="Red fabric banner hanging between two gold rods with scattered confetti"></div>
    <h1 class="banner-title">
      <span class="title-grand">GRAND</span>
      <span class="title-opening">Opening</span>
    </h1>

    <p class="invite-text">Come celebrate the grand opening of our state-of-the-art robotic physical therapy office! Our cutting-edge technology and highly skilled therapists provide personalized treatment plans to help you recover faster and more efficiently.</p>

    <section class="detail detail-event">
      <h2 class="detail-label">Event:</h2>
      <p class="detail-value">Thursday, June 1st, 2023 from 12pm-6pm</p>
    </section>

    <section class="detail detail-location">
      <h2 class="detail-label">Location:</h2>
      <p class="detail-value">58274 Harlow Ave, Bloomfield Hills, MI 48319</p>
    </section>
  </main>
</body>
</html>
```